Bref créative
Business card desin for auto parts seller
Ridgeline Parts Company
Modern
Dale Merriweather
President
1187 Cedar Hollow Ln
Pine Harbor, NC 30642
dale@ridgelinepartscompany.com
www.ridgelinepartscompany.com

```html
<!DOCTYPE html>
<html lang="en">
<head>
<meta charset="utf-8">
<title>Ridgeline Parts Company — Business Card</title>
<link rel="stylesheet" href="https://fonts.googleapis.com/css2?family=Oswald:wght@400;600;700&family=Black+Ops+One&display=swap">
<style>
  :root {
    --backdrop: #232323;
    --card-black: #0b0b0b;
    --gold: #c9a766;
    --gold-soft: #d8bd85;
    --ink: #0b0b0b;
    --white: #f3f0ea;
  }
  * { box-sizing: border-box; margin: 0; padding: 0; }
  html, body { width: 1200px; height: 698px; overflow: hidden; }
  body {
    background: var(--backdrop);
    font-family: "Oswald", sans-serif;
    position: relative;
  }
  .card {
    position: absolute;
    top: 206px;
    width: 500px;
    height: 286px;
    border-radius: 14px;
    overflow: hidden;
    background: var(--card-black);
    box-shadow: 0 10px 30px rgba(0,0,0,.5);
  }
  .card--front { left: 60px; }
  .card--back { left: 640px; }

  .track-area {
    position: absolute;
    background: linear-gradient(135deg, var(--gold-soft), var(--gold));
  }
  .card--front .track-area--top { left: 0; top: 0; width: 150px; height: 130px; clip-path: polygon(0 0, 100% 0, 40% 100%, 0 100%); opacity: .85; }
  .card--front .track-area--bottom { left: 0; bottom: 0; width: 500px; height: 92px; clip-path: polygon(0 30%, 100% 0, 100% 100%, 0 100%); }

  .brand {
    position: absolute;
    display: flex;
    align-items: center;
    gap: 10px;
  }
  .brand__dot {
    width: 56px; height: 56px; border-radius: 50%;
    background: var(--gold);
    flex: none;
  }
  .brand__name {
    font-weight: 700;
    text-transform: uppercase;
    line-height: 1.05;
    font-size: 24px;
  }
  .card--front .brand { left: 190px; top: 62px; }
  .card--front .brand__name { color: var(--gold); }

  .web {
    position: absolute;
    left: 30px; top: 168px;
    font-size: 21px;
    font-weight: 600;
    color: var(--gold);
    letter-spacing: .5px;
  }

  .card--back .track-area--panel {
    left: 0; top: 110px; width: 290px; height: 176px;
    clip-path: polygon(0 14%, 88% 0, 100% 100%, 0 100%);
  }
  .card--back .brand { left: 28px; top: 188px; }
  .card--back .brand__dot { background: var(--ink); }
  .card--back .brand__name { color: var(--ink); font-size: 22px; }

  .person {
    position: absolute;
    right: 26px; top: 22px;
    text-align: right;
  }
  .person__name {
    font-family: "Black Ops One", sans-serif;
    font-weight: 400;
    font-size: 27px;
    color: var(--white);
  }
  .person__title {
    font-size: 13px;
    color: var(--gold);
    text-transform: uppercase;
    letter-spacing: 2px;
  }
  .contact {
    position: absolute;
    right: 26px; top: 100px;
    text-align: right;
    color: var(--white);
    font-size: 12px;
    line-height: 1.55;
    font-weight: 400;
  }
  .contact__gap { height: 8px; }
</style>
</head>
<body>

  <section class="card card--front" aria-label="Card front">
    <div class="track-area track-area--top" role="img" aria-label="Gold tire track texture"></div>
    <div class="track-area track-area--bottom" role="img" aria-label="Gold tire track texture band"></div>
    <div class="brand">
      <span class="brand__dot"></span>
      <span class="brand__name">Ridgeline<br>Parts Company</span>
    </div>
    <p class="web">www.ridgelinepartscompany.com</p>
  </section>

  <section class="card card--back" aria-label="Card back">
    <div class="track-area track-area--panel" role="img" aria-label="Gold panel with tire track texture"></div>
    <div class="person">
      <h1 class="person__name">Dale Merriweather</h1>
      <p class="person__title">President</p>
    </div>
    <div class="contact">
      <p>1187 Cedar Hollow Ln</p>
      <p>Pine Harbor, NC 30642</p>
      <div class="contact__gap"></div>
      <p>706-555-0142 Cell</p>
      <p>706-555-0187 Office</p>
      <div class="contact__gap"></div>
      <p>dale@ridgelinepartscompany.com</p>
      <p>www.ridgelinepartscompany.com</p>
    </div>
    <div class="brand">
      <span class="brand__dot"></span>
      <span class="brand__name">Ridgeline<br>Parts Company</span>
    </div>
  </section>

</body>
</html>
```